KT Crewing business card

Require business card which includes:
Company name: KT CREWING PTY LTD
Email: Mick@ktcrewing.com.au
Phone: 0431 556 208
ACN: 517 238 649

slogan: Onsite Auto Electrician Labour hire

Details and logo on top side
Logo only on bottom side

colour codes : #F15A29 , #939598

Target Market(s)

Western Australia mining sector

Industry/Entity Type

Mining

Contact Information for Business Card

Require business card which includes: Company name: KT CREWING PTY LTD Email: Mick@ktcrewing.com.au Phone: 0431 556 208 ACN: 517 238 649 slogan: Onsite Auto Electrician Labour hire Details and logo on top side Logo only on bottom side colour codes : #F15A29 , #939598

Colors
EE7325
F08F49
F5BC92
FAE3D3
FDF4ED

Requirements
Must have
• double sided

```html
<!DOCTYPE html>
<html lang="en">
<head>
<meta charset="UTF-8">
<title>KT Crewing Business Card</title>
<link href="https://fonts.googleapis.com/css2?family=Montserrat:wght@400;500;700;800&display=swap" rel="stylesheet">
<style>
  :root {
    --orange: #F15A29;
    --grey: #939598;
    --ink: #1c1c1c;
    --paper: #ffffff;
    --backdrop: #2b2d2c;
  }
  * { margin: 0; padding: 0; box-sizing: border-box; }
  html, body {
    width: 1200px;
    height: 910px;
    overflow: hidden;
    background: var(--backdrop);
    font-family: "Montserrat", Arial, sans-serif;
  }
  .sheet {
    width: 1200px;
    height: 910px;
    display: flex;
    flex-direction: column;
    align-items: center;
    justify-content: center;
    gap: 44px;
  }
  .card {
    position: relative;
    width: 640px;
    height: 366px;
    background: var(--paper);
    box-shadow: 0 8px 22px rgba(0,0,0,0.45);
    overflow: hidden;
  }
  .wordmark {
    display: flex;
    align-items: center;
    justify-content: center;
    gap: 14px;
  }
  .wordmark-square {
    background: var(--grey);
    flex: none;
  }
  .wordmark-name {
    color: var(--orange);
    font-weight: 800;
    letter-spacing: -0.5px;
    line-height: 1;
    white-space: nowrap;
  }
  /* logo-only side */
  .card--back .wordmark {
    position: absolute;
    inset: 0;
  }
  .card--back .wordmark-square { width: 46px; height: 46px; }
  .card--back .wordmark-name { font-size: 62px; }

  /* details side */
  .card--front .wordmark {
    position: absolute;
    top: 66px;
    left: 0;
    right: 0;
  }
  .card--front .wordmark-square { width: 34px; height: 34px; }
  .card--front .wordmark-name { font-size: 46px; }

  .company {
    position: absolute;
    top: 168px;
    left: 0;
    right: 0;
    text-align: center;
  }
  .company-name {
    font-size: 23px;
    font-weight: 800;
    letter-spacing: 0.2px;
    color: var(--orange);
  }
  .company-name .legal { color: var(--grey); }
  .slogan {
    margin-top: 6px;
    font-size: 16px;
    font-weight: 500;
    color: var(--ink);
  }
  .contact-band {
    position: absolute;
    left: 0;
    right: 0;
    top: 284px;
    height: 46px;
    background: var(--orange);
    display: flex;
    align-items: center;
    justify-content: center;
    gap: 16px;
    color: var(--paper);
    font-size: 15.5px;
    font-weight: 500;
  }
  .contact-item {
    display: flex;
    align-items: center;
    gap: 7px;
    white-space: nowrap;
  }
  .contact-icon { width: 17px; height: 17px; flex: none; }
</style>
</head>
<body>
<main class="sheet">

  <section class="card card--back" aria-label="Card reverse side">
    <div class="wordmark">
      <span class="wordmark-square"></span>
      <span class="wordmark-name">KT Crewing</span>
    </div>
  </section>

  <section class="card card--front" aria-label="Card front side">
    <div class="wordmark">
      <span class="wordmark-square"></span>
      <span class="wordmark-name">KT Crewing</span>
    </div>

    <div class="company">
      <p class="company-name">KT CREWING <span class="legal">PTY LTD</span></p>
      <p class="slogan">Onsite Auto Electrician Labour hire</p>
    </div>

    <div class="contact-band">
      <span class="contact-item">
        <svg class="contact-icon" viewBox="0 0 24 24" aria-hidden="true">
          <path fill="#fff" d="M6.6 10.8c1.4 2.8 3.8 5.1 6.6 6.6l2.2-2.2c.3-.3.7-.4 1-.2 1.1.4 2.3.6 3.6.6.6 0 1 .4 1 1V20c0 .6-.4 1-1 1C10.6 21 3 13.4 3 4c0-.6.4-1 1-1h3.5c.6 0 1 .4 1 1 0 1.3.2 2.5.6 3.6.1.3 0 .7-.2 1L6.6 10.8z"/>
        </svg>
        0431 556 208
      </span>
      <span class="contact-item">
        <svg class="contact-icon" viewBox="0 0 24 24" aria-hidden="true">
          <rect x="2" y="5" width="20" height="14" fill="#fff"/>
          <path d="M2 5l10 8 10-8" fill="none" stroke="#F15A29" stroke-width="1.6"/>
        </svg>
        Mick@ktcrewing.com.au
      </span>
      <span class="contact-item">ACN: 517 238 649</span>
    </div>
  </section>

</main>
</body>
</html>
```